Business Card Design Project

I have attached the logo and the colour pallete for the branding for the company.

Creative designs for business cards are needed.

The Company is modern corporate.

Industry/Entity Type

Business

```html
<!DOCTYPE html>
<html lang="en">
<head>
<meta charset="utf-8">
<title>Business Card – Front and Back</title>
<link rel="stylesheet" href="https://fonts.googleapis.com/css2?family=Source+Sans+3:ital,wght@0,700;1,700&display=swap">
<style>
  :root {
    --page-bg: #ffffff;
    --card-fill: #414042;
    --ink-dark: #0d0d0d;
    --ink-light: #f7f7f5;
  }
  html, body {
    margin: 0;
    padding: 0;
    width: 1200px;
    height: 1000px;
    overflow: hidden;
    background: var(--page-bg);
  }
  .canvas {
    display: block;
    width: 1200px;
    height: 1000px;
    font-family: "Source Sans 3", "Myriad Pro", Arial, sans-serif;
    font-weight: 700;
  }
  .card-shape { fill: var(--card-fill); }
  .wordmark {
    fill: var(--ink-light);
    font-weight: 700;
    letter-spacing: -0.01em;
  }
  .wordmark--small { font-size: 96px; }
  .wordmark--large { font-size: 190px; }
  .client-name {
    fill: var(--ink-dark);
    font-size: 38px;
  }
  .client-role {
    fill: var(--ink-dark);
    font-size: 27px;
    font-style: italic;
  }
  .contact-item {
    fill: var(--ink-dark);
    font-size: 27px;
  }
  .contact-divider {
    stroke: var(--ink-dark);
    stroke-width: 2.5;
  }
</style>
</head>
<body>
<svg class="canvas" width="1200" height="1000" viewBox="0 0 1200 1000" role="img" aria-label="Business card front and back for kiravue">
  <g class="card card--front">
    <path class="card-shape" d="M221,53 H762 A220,220 0 0 1 982,273 V493 H441 A220,220 0 0 1 221,273 Z"/>
    <text class="wordmark wordmark--small" x="236" y="148" textLength="329" lengthAdjust="spacing">kiravue</text>
    <text class="client-name" x="958" y="340" text-anchor="end">Name of the client</text>
    <text class="client-role" x="958" y="366" text-anchor="end">Profession</text>
    <text class="contact-item contact-phone" x="632" y="432" text-anchor="end">Contact No.</text>
    <line class="contact-divider" x1="680" y1="409" x2="680" y2="438"/>
    <text class="contact-item contact-email" x="958" y="432" text-anchor="end">Email Add@email</text>
  </g>

  <g class="card card--back">
    <path class="card-shape" d="M441,507 H982 V725 A220,220 0 0 1 762,945 H221 V727 A220,220 0 0 1 441,507 Z"/>
    <text class="wordmark wordmark--large" x="280" y="798" textLength="655" lengthAdjust="spacing">kiravue</text>
  </g>
</svg>
</body>
</html>
```